Cellar Crew Poster / Flyer Ad Design

We need a poster design (and a complimentary A6 flyer) to promote our Adult Rock Band Course called 'Cellar Crew'.

Target market is adults aged 25 - 50 primarily

Design to be eye catching, creative, appealing and easy to understand. Most of the distribution will be street marketing, email marketing, social media, music magazines and websites and to other music teachers.

We need the design to be as an A3 and A4 poster and an A6 promo flyer/e-flyer. Should look good in colour and we'll want a version in black and white.

Would be good to also incorporate our music school logo (just for branding purposes).

Text as follows:

CELLAR CREW
The Ultimate Rock Band Course for Adults

Ever wondered what it would be like to play in a band?

Feeling musically rusty and looking for a way to start playing your instrument again?

Then here’s an exciting opportunity you can’t miss!

All musical levels
Beginner/Intermediate to Advanced Players

Limited Numbers

REGISTER ONLINE NOW
www.tunewellstudio.com.au

Starts Saturday 3rd August
Newtown

Over 6 exciting weekends you’ll work with one of our experienced professional band coaches and transform yourselves into the ultimate ‘Cellar Crew’

Discover how to play in a band
Revisit your musical abilities
Practice songs
Perform on Stage

Drummers, Bass Guitarists, Singers, Keys, Guitarists, Saxophone, Percussionists and others all welcome to join

For more information, course costs and registration, please visit www.tunewellstudio.com.au or call 02 7391 4825 / 0438 572 904

Reason: Hi Everyone, I've been away and unable to respond to some of the designs because I've been ill. Have decided to extend the deadline and now commit to paying designers. Look forward to seeing more designs. Any questions, please let me know. Thanks Melinda

```html
<!DOCTYPE html>
<html lang="en">
<head>
<meta charset="utf-8">
<title>Cellar Crew – The Ultimate Rock Band Course for Adults</title>
<link href="https://fonts.googleapis.com/css2?family=Rubik+Dirt&family=Kaushan+Script&family=Tinos:wght@400;700&display=swap" rel="stylesheet">
<style>
  :root {
    --ink: #000000;
    --paper: #ffffff;
    --band: rgba(0, 0, 0, 0.55);
    --stage-warm: #b07a4c;
    --stage-deep: #3a2416;
    --stage-light: #e0c7a5;
    --drum-light: #8a8a8a;
    --drum-dark: #1c1c1c;
  }
  html, body { margin: 0; padding: 0; overflow: hidden; background: var(--ink); }
  .poster {
    position: relative;
    width: 849px; height: 1200px;
    background: var(--ink);
    color: var(--paper);
    overflow: hidden;
    font-family: "Tinos", "Times New Roman", serif;
  }
  .abs { position: absolute; }
  .stage-photo {
    left: 0; top: 245px; width: 805px; height: 680px;
    background:
      radial-gradient(circle at 60% 50%, var(--stage-light) 0 9%, transparent 22%),
      radial-gradient(ellipse at 55% 60%, var(--stage-warm) 0%, var(--stage-deep) 70%, #120a05 100%);
    clip-path: polygon(22% 8%, 58% 4%, 60% 0, 100% 6%, 100% 72%, 90% 80%, 78% 100%, 0 100%, 0 62%, 4% 56%, 22% 54%, 24% 30%, 20% 25%);
  }
  .drum-photo {
    left: 180px; top: 730px; width: 669px; height: 470px;
    background: radial-gradient(ellipse at 70% 55%, var(--drum-light) 0%, #4a4a4a 45%, var(--drum-dark) 100%);
    clip-path: polygon(30% 0, 100% 4%, 100% 100%, 0 100%, 0 40%, 12% 30%);
  }
  .title {
    left: 0; width: 849px; top: 50px; margin: 0;
    text-align: center;
    font-family: "Rubik Dirt", "Impact", sans-serif;
    font-size: 96px; font-weight: 400; letter-spacing: 2px; line-height: 1;
  }
  .subtitle {
    left: 0; width: 849px; top: 148px; margin: 0;
    text-align: center;
    font-family: "Kaushan Script", cursive;
    font-size: 43px; font-weight: 400; letter-spacing: -0.5px;
  }
  .intro { left: 32px; top: 250px; margin: 0; font-size: 25px; line-height: 1.2; }
  .intro p { margin: 0 0 13px; }
  .benefits {
    left: 0; top: 583px; width: 360px; padding: 6px 0 6px 28px;
    list-style: none; margin: 0; background: var(--band);
    font-size: 22.5px; line-height: 30.5px;
  }
  .levels { right: 40px; top: 666px; text-align: right; }
  .levels-head { font-family: "Kaushan Script", cursive; font-size: 40px; line-height: 1; }
  .levels-sub { font-size: 17px; margin-top: 4px; }
  .starts {
    left: 30px; top: 714px;
    font-family: "Kaushan Script", cursive; font-size: 54px; line-height: 1;
    -webkit-text-stroke: 1px var(--ink);
  }
  .date-banner {
    left: 0; top: 760px; width: 560px; height: 90px;
    background: var(--paper);
    clip-path: polygon(0 14%, 100% 0, 98% 92%, 0 100%);
  }
  .date {
    left: 8px; top: 776px; color: var(--ink);
    font-family: "Kaushan Script", cursive; font-size: 58px; line-height: 1; letter-spacing: -1.5px;
    transform: rotate(-1.5deg);
  }
  .venue {
    left: 254px; top: 848px; padding: 0 12px 4px;
    background: var(--paper); color: var(--ink);
    font-family: "Kaushan Script", cursive; font-size: 52px; line-height: 1; letter-spacing: -1px;
    transform: rotate(-1.5deg);
  }
  .details {
    left: 0; top: 927px; width: 749px; padding: 4px 0 4px 29px;
    background: var(--band); font-size: 22.5px; line-height: 27px; margin: 0;
  }
  .crew-name { left: 28px; top: 990px; font-family: "Kaushan Script", cursive; font-size: 32px; }
  .players {
    left: 0; top: 1030px; width: 720px; padding: 2px 0 2px 29px;
    background: var(--band); font-size: 22.5px; line-height: 27px; margin: 0;
  }
  .register { left: 28px; top: 1088px; font-size: 25px; font-weight: 700; margin: 0; }
  .register-url { left: 28px; top: 1116px; font-size: 22px; }
  .more-info { left: 27px; top: 1141px; font-size: 15.7px; line-height: 19px; margin: 0; }
  .brand { left: 556px; top: 1144px; }
  .brand-name { font-size: 27px; font-weight: 700; color: var(--paper); }
</style>
</head>
<body>
<div class="poster">
  <div class="abs stage-photo" role="img" aria-label="Photo: close-up of a stage microphone in front of a blurred concert crowd"></div>
  <div class="abs drum-photo" role="img" aria-label="Black and white photo: hands playing a drum kit"></div>

  <h1 class="abs title">CELLAR CREW</h1>
  <p class="abs subtitle">The Ultimate Rock Band Course for Adults</p>

  <div class="abs intro">
    <p>Ever wondered what it would be like to play in a band?</p>
    <p>Feeling musically rusty and looking for a way<br>to start playing your instrument again?</p>
    <p>Then here’s an exciting opportunity you can’t miss!</p>
  </div>

  <ul class="abs benefits">
    <li>Discover how to play in a band</li>
    <li>Revisit your musical abilities</li>
    <li>Practice songs</li>
    <li>Perform on Stage</li>
  </ul>

  <div class="abs levels">
    <div class="levels-head">All musical levels</div>
    <div class="levels-sub">Beginner/Intermediate to Advanced Players</div>
  </div>

  <div class="abs starts">Starts</div>
  <div class="abs date-banner"></div>
  <div class="abs date">Saturday 3rd August</div>
  <div class="abs venue">Newtown</div>

  <p class="abs details">Over 6 exciting weekends you’ll work with one of our experienced<br>professional band coaches and transform yourselves into the ultimate</p>
  <div class="abs crew-name">‘Cellar Crew’</div>
  <p class="abs players">Drummers, Bass Guitarists, Singers, Keys, Guitarists,<br>Saxophone, Percussionists and others all welcome to join</p>

  <p class="abs register">Register Online Now</p>
  <div class="abs register-url">www.tunewellstudio.com.au</div>
  <p class="abs more-info">For more information, course costs and registration, please visit<br>www.tunewellstudio.com.au or call 02 7391 4825 / 0438 572 904</p>

  <div class="abs brand">
    <span class="brand-name">Tunewell Studio</span>
  </div>
</div>
</body>
</html>
```